Creative Challenge - Disruptive Digital Construction Business needs an Application Design

We need an application design (4 screens).
The app will offer easy-to-use an interactive course to illustrate the latest technology to construction professionals. Kindly find the attachments.
Updates

I have just posted the contest and the deadline is tomorrow!! Please give me my original 7 days back.

Need extra days to review

Target Market(s)

Construction professionals, aged from 22 to 36, who want to learn new disruptive technologies in construction.

Colors
e667a6
b868aa
33a6d7

Requirements
Must have
• The name of the app, Velunor, stands for “Brightframe Skill Voyagers”. The user is a Velunor, who would transform the digital construction industry. We want a design that gives that feel to the users.

```html
<!DOCTYPE html>
<html lang="en">
<head>
<meta charset="utf-8">
<title>Velunor – Home</title>
<link href="https://fonts.googleapis.com/css2?family=Inter:wght@400;500&family=Roboto:wght@700;900&display=swap" rel="stylesheet">
<style>
  :root {
    --brand-blue: #33a6d7;
    --icon-blue: #34a7d8;
    --canvas: #ffffff;
    --screen-bg: #ffffff;
    --card-bg: #ffffff;
    --text-dark: #2b2b33;
    --text-light: #ffffff;
    --menu-grey: #6b6478;
    --bell-grey: #b7b2bd;
    --alert-pink: #f0436e;
  }
  * { box-sizing: border-box; margin: 0; padding: 0; }
  html, body { width: 1200px; height: 1000px; overflow: hidden; background: var(--canvas); }
  body { position: relative; font-family: "Inter", Arial, sans-serif; }

  .app-screen {
    position: absolute; left: 400px; top: 42px; width: 399px; height: 916px;
    background: var(--screen-bg);
    box-shadow: 0 10px 40px rgba(0,0,0,0.16);
    overflow: hidden;
  }
  .app-header {
    position: absolute; left: 0; top: 0; width: 100%; height: 159px;
    background: var(--brand-blue); color: var(--text-light);
    box-shadow: 0 6px 14px rgba(51,166,215,0.18);
  }
  .status-bar {
    position: absolute; left: 16px; right: 16px; top: 14px; height: 16px;
    display: flex; justify-content: space-between; align-items: center;
    font-size: 12px; font-weight: 500;
  }
  .status-left, .status-right { display: flex; align-items: center; gap: 5px; }
  .round-button {
    position: absolute; top: 63px; width: 43px; height: 43px; border-radius: 50%;
    background: #fff; display: flex; align-items: center; justify-content: center;
    box-shadow: 0 3px 8px rgba(0,0,0,0.12);
  }
  .menu-button { left: 22px; }
  .bell-button { left: 334px; }
  .greeting {
    position: absolute; left: 0; width: 100%; top: 69px; text-align: center;
    font-family: "Roboto", Arial, sans-serif; font-weight: 900; font-size: 25px;
  }
  .tagline {
    position: absolute; left: 0; width: 100%; top: 109px; text-align: center;
    font-size: 16px; font-weight: 500;
  }

  .topic-list { position: absolute; left: 20px; top: 177px; width: 358px; list-style: none; }
  .topic-card {
    height: 104px; margin-bottom: 17.4px; background: var(--card-bg); border-radius: 3px;
    box-shadow: 0 4px 14px rgba(0,0,0,0.09);
    display: flex; align-items: center; padding-left: 28px;
  }
  .topic-icon {
    width: 68px; height: 68px; border-radius: 50%; background: var(--icon-blue);
    display: flex; align-items: center; justify-content: center; flex-shrink: 0;
  }
  .topic-label {
    margin-left: 20px; font-size: 16px; line-height: 25.5px; color: var(--text-dark);
  }
</style>
</head>
<body>
  <main class="app-screen">
    <header class="app-header">
      <div class="status-bar">
        <div class="status-left">
          <svg width="34" height="7" viewBox="0 0 34 7" fill="#fff" stroke="#fff">
            <circle cx="3.5" cy="3.5" r="3"/><circle cx="10.5" cy="3.5" r="3"/><circle cx="17.5" cy="3.5" r="3"/>
            <circle cx="24.5" cy="3.5" r="2.6" fill="none"/><circle cx="31" cy="3.5" r="2.6" fill="none"/>
          </svg>
          <span>GS</span>
          <svg width="14" height="11" viewBox="0 0 14 11" fill="none" stroke="#fff" stroke-width="1.6" stroke-linecap="round">
            <path d="M1 4a9 9 0 0 1 12 0"/><path d="M3.3 6.3a5.5 5.5 0 0 1 7.4 0"/><circle cx="7" cy="9" r="1" fill="#fff"/>
          </svg>
        </div>
        <div class="status-right">
          <span>58 %</span>
          <svg width="26" height="12" viewBox="0 0 26 12">
            <rect x="0.5" y="0.5" width="22" height="11" rx="2.5" fill="none" stroke="#fff"/>
            <rect x="2" y="2" width="11" height="8" rx="1" fill="#fff"/>
            <rect x="23.5" y="4" width="1.6" height="4" rx="0.8" fill="#fff"/>
          </svg>
        </div>
      </div>

      <div class="round-button menu-button" aria-label="Menu">
        <svg width="16" height="12" viewBox="0 0 16 12" stroke="var(--menu-grey)" stroke-width="1.6">
          <path d="M0 1h16M0 6h16M0 11h16"/>
        </svg>
      </div>
      <h1 class="greeting">Hello! Velunor</h1>
      <p class="tagline">Your Journey Starts Here...</p>
      <div class="round-button bell-button" aria-label="Notifications">
        <svg width="20" height="20" viewBox="0 0 20 20">
          <path d="M10 2a5 5 0 0 0-5 5v4l-2 3h14l-2-3V7a5 5 0 0 0-5-5z" fill="var(--bell-grey)"/>
          <rect x="8" y="15" width="4" height="2.5" rx="1.2" fill="var(--bell-grey)"/>
          <circle cx="14.5" cy="4.5" r="4" fill="var(--alert-pink)"/>
        </svg>
      </div>
    </header>

    <ul class="topic-list">
      <li class="topic-card">
        <span class="topic-icon">
          <svg width="30" height="30" viewBox="0 0 30 30">
            <g fill="#fff">
              <circle cx="15" cy="15" r="9.5"/>
              <rect x="12.5" y="2" width="5" height="26" rx="1.5"/>
              <rect x="12.5" y="2" width="5" height="26" rx="1.5" transform="rotate(45 15 15)"/>
              <rect x="12.5" y="2" width="5" height="26" rx="1.5" transform="rotate(90 15 15)"/>
              <rect x="12.5" y="2" width="5" height="26" rx="1.5" transform="rotate(135 15 15)"/>
            </g>
            <circle cx="15" cy="15" r="5" fill="var(--icon-blue)"/>
          </svg>
        </span>
        <span class="topic-label">Customize Your<br>Journey</span>
      </li>
      <li class="topic-card">
        <span class="topic-icon">
          <svg width="28" height="28" viewBox="0 0 28 28" fill="#fff">
            <path d="M24 4c-6 0-11 3-14 9l5 5c6-3 9-8 9-14z"/>
            <path d="M9 11H5l-3 4h6zM17 19v4l-4 3v-6z"/>
            <path d="M8 18c-2 1-3 4-3 5 1 0 4-1 5-3z"/>
            <circle cx="18" cy="10" r="2" fill="var(--icon-blue)"/>
          </svg>
        </span>
        <span class="topic-label">How to Start BIM?</span>
      </li>
      <li class="topic-card">
        <span class="topic-icon">
          <svg width="28" height="28" viewBox="0 0 28 28" fill="#fff">
            <rect x="7" y="4" width="5" height="5" rx="1"/><rect x="16" y="4" width="5" height="5" rx="1"/>
            <path d="M6 10h7v14H3v-6zM15 10h7l3 8v6H15z"/>
            <rect x="12.5" y="11" width="3" height="5"/>
          </svg>
        </span>
        <span class="topic-label">Important ISO19650<br>principles to know</span>
      </li>
      <li class="topic-card">
        <span class="topic-icon">
          <svg width="26" height="28" viewBox="0 0 26 28">
            <path d="M13 2c1 5 9 9 9 16a9 9 0 0 1-18 0c0-4 2-6 4-8 0 3 1 4 2 4 0-5 1-9 3-12z" fill="#fff"/>
            <path d="M13 13c2 3 4 4 4 7a4 4 0 0 1-8 0c0-3 2-4 4-7z" fill="var(--icon-blue)"/>
          </svg>
        </span>
        <span class="topic-label">Information Management<br>Processes &amp; Activities</span>
      </li>
      <li class="topic-card">
        <span class="topic-icon">
          <svg width="28" height="26" viewBox="0 0 28 26">
            <path d="M2 3h9a3 3 0 0 1 3 2 3 3 0 0 1 3-2h9v17h-9l-3 3-3-3H2z" fill="#fff"/>
            <g stroke="var(--icon-blue)" stroke-width="1.6">
              <path d="M5 8h6M5 11.5h6M5 15h6M17 8h6M17 11.5h6M17 15h6"/>
              <path d="M14 6v14"/>
            </g>
          </svg>
        </span>
        <span class="topic-label">Documents/Resources<br>You Need to Develop</span>
      </li>
      <li class="topic-card">
        <span class="topic-icon">
          <svg width="28" height="26" viewBox="0 0 28 26">
            <path d="M14 2 27 8v16H1V8z" fill="#fff"/>
            <rect x="6" y="11" width="16" height="13" fill="var(--icon-blue)"/>
            <g fill="#fff"><rect x="7.5" y="12.5" width="13" height="2.2"/><rect x="7.5" y="16" width="13" height="2.2"/><rect x="7.5" y="19.5" width="13" height="2.2"/></g>
          </svg>
        </span>
        <span class="topic-label">Other Resources</span>
      </li>
    </ul>
  </main>
</body>
</html>
```